Social Media Graphics - Copperfield Loop

Create 6-7 individual social media graphics (square size) to encourage folks to join our online course, using either of the text below (only one set of text per graphic:

The Lantern Ridge Method
How to Create a 7-Figure Business From Scratch
Sign Up Today!

Or

The Lantern Ridge Method
Fast-track Your Way to a Multi-Million Business!
Sign Up Today!

For the color scheme of the graphics, use 1 or 2 colors in the color palette attached; or use any colors that look nice with their outfits; AVOID using red, white and blue altogether because it will look like an Independence Day (4th of July) graphic and we don’t want that; make sure the graphics appeal to both men and women

Make sure each graphic contains 1 of the 2 pics attached; and make sure one of the graphics is all TEXT only.

Target Market(s)

men and women looking to make more money

Industry/Entity Type

entrepreneurship

Requirements
Must have
• see the text document attached
Nice to have
• We are open to a nice color design; the color palette colors are not required, especially we don't want red, white and blue used together
Should not have
• AVOID using red, white and blue altogether because it will look like an Independence Day (4th of July) graphic and we dont want that

```html
<!DOCTYPE html>
<html lang="en">
<head>
<meta charset="utf-8">
<title>The Lantern Ridge Method – Sign Up Today</title>
<link rel="stylesheet" href="https://fonts.googleapis.com/css2?family=Barlow+Condensed:ital,wght@0,500;0,600;0,700;1,800&family=Poppins:wght@800&display=swap">
<style>
  :root {
    --page: #fbf8f2;
    --cream-light: #fbf3e3;
    --cream-deep: #f1dfbf;
    --emerald: #0f6650;
    --gold: #d49a2a;
    --forest: #0c3a31;
    --ivory: #fff7e8;
    --gold-dot: #e8b54a;
  }
  html, body {
    margin: 0;
    padding: 0;
    width: 1200px;
    height: 1200px;
    overflow: hidden;
    background: var(--page);
  }
  .canvas {
    display: block;
    width: 1200px;
    height: 1200px;
  }
  .condensed { font-family: "Barlow Condensed", "Arial Narrow", sans-serif; }
  .title-the, .title-name { font-style: italic; font-weight: 800; }
  .title-the { fill: var(--emerald); }
  .title-name { fill: var(--ivory); }
  .title-method { fill: var(--emerald); font-weight: 600; }
  .lead-in { fill: var(--ivory); font-weight: 500; }
  .seven { fill: var(--forest); font-weight: 500; }
  .figure-word { fill: var(--ivory); font-weight: 600; }
  .subline { fill: var(--ivory); font-weight: 700; }
  .cta {
    font-family: "Poppins", "Arial Black", sans-serif;
    font-weight: 800;
    fill: var(--forest);
  }
  .panel-fill { fill: url(#panelGradient); }
  .name-band { fill: var(--gold); }
  .accent-stripe { fill: var(--emerald); }
  .promise-band { fill: var(--forest); }
  .dot-rule { stroke: var(--gold-dot); stroke-width: 3; stroke-dasharray: 2 5; stroke-linecap: round; }
</style>
</head>
<body>
<svg class="canvas" viewBox="0 0 1200 1200" xmlns="http://www.w3.org/2000/svg">
  <defs>
    <linearGradient id="panelGradient" gradientUnits="userSpaceOnUse" x1="131" y1="131" x2="1080" y2="1080">
      <stop offset="0" style="stop-color:#fbf3e3"/>
      <stop offset="1" style="stop-color:#f1dfbf"/>
    </linearGradient>
    <clipPath id="bandClip">
      <rect x="131" y="621" width="949" height="321"/>
    </clipPath>
  </defs>

  <rect class="panel-fill" x="131" y="131" width="949" height="949"/>

  <g class="course-title condensed">
    <text class="title-the" x="212" y="371" font-size="237" textLength="266" lengthAdjust="spacingAndGlyphs">THE</text>
    <polygon class="accent-stripe" points="534,177 540,177 487,388 480,388"/>
    <polygon class="name-band" points="539,177 1080,177 1080,388 491,388"/>
    <text class="title-name" x="792" y="276" font-size="104" text-anchor="middle">LANTERN</text>
    <text class="title-name" x="774" y="364" font-size="104" text-anchor="middle">RIDGE</text>
    <text class="title-method" x="606" y="570" font-size="220" text-anchor="middle">METHOD</text>
  </g>

  <g class="promise condensed">
    <rect class="promise-band" x="131" y="621" width="949" height="321"/>
    <ellipse class="panel-fill" cx="417" cy="781" rx="94" ry="175" clip-path="url(#bandClip)"/>
    <text class="lead-in" x="182" y="717" font-size="90" textLength="124" lengthAdjust="spacingAndGlyphs">HOW</text>
    <text class="lead-in" x="181" y="848" font-size="163" textLength="113" lengthAdjust="spacingAndGlyphs">TO</text>
    <text class="lead-in" x="181" y="909" font-size="57" textLength="128" lengthAdjust="spacingAndGlyphs">CREATE</text>
    <text class="seven" x="363" y="915" font-size="356" textLength="102" lengthAdjust="spacingAndGlyphs">7</text>
    <text class="figure-word" x="539" y="824" font-size="242" textLength="482" lengthAdjust="spacingAndGlyphs">FIGURE</text>
    <line class="dot-rule" x1="540" y1="851" x2="1020" y2="851"/>
    <text class="subline" x="538" y="909" font-size="49" textLength="480" lengthAdjust="spacingAndGlyphs">BUSINESS FROM SCRATCH</text>
  </g>

  <text class="cta" x="604" y="1038" font-size="72" text-anchor="middle" textLength="592" lengthAdjust="spacingAndGlyphs">SIGN UP TODAY!</text>
</svg>
</body>
</html>
```